Creative & Professional Business Card for hair salon

We are looking to update our business cards. Our salon is creative, modern, progressive and professional and looking for a design that will reflect this.

```html
<!DOCTYPE html>
<html lang="en">
<head>
<meta charset="utf-8">
<title>Crowns in the Sky – Business Card</title>
<link rel="stylesheet" href="https://fonts.googleapis.com/css2?family=Josefin+Sans:wght@300&family=Dosis:wght@300&display=swap">
<style>
  :root {
    --page: #ffffff;
    --card: #e9e9eb;
    --frame: #6fa3c0;
    --rule: #8fb0c2;
    --brand: #4c7391;
    --contact: #2d5886;
  }
  * { margin: 0; padding: 0; box-sizing: border-box; }
  html, body {
    width: 1200px;
    height: 804px;
    overflow: hidden;
    background: var(--page);
  }
  .canvas {
    position: relative;
    width: 1200px;
    height: 804px;
  }
  .card {
    position: absolute;
    left: 40px;
    top: 40px;
    width: 1120px;
    height: 725px;
    background: var(--card);
  }
  .frame {
    position: absolute;
    left: 0;
    top: 0;
    width: 1200px;
    height: 804px;
  }
  .brand {
    position: absolute;
    left: 0;
    top: 250px;
    width: 1200px;
    text-align: center;
    color: var(--brand);
    font-family: "Josefin Sans", sans-serif;
    font-weight: 300;
  }
  .brand-name {
    font-size: 62px;
    line-height: 1;
    letter-spacing: 0.5px;
  }
  .brand-owner {
    margin-top: 34px;
    font-size: 30px;
    letter-spacing: 2px;
  }
  .divider {
    position: absolute;
    left: 251px;
    top: 520px;
    width: 698px;
    height: 1.5px;
    background: var(--rule);
  }
  .contact {
    position: absolute;
    left: 0;
    width: 1200px;
    text-align: center;
    color: var(--contact);
    font-family: "Dosis", sans-serif;
    font-weight: 300;
  }
  .contact-address {
    top: 552px;
    font-size: 42px;
    letter-spacing: 3.5px;
  }
  .contact-web {
    top: 617px;
    font-size: 30px;
    letter-spacing: 2.5px;
  }
</style>
</head>
<body>
  <main class="canvas">
    <div class="card"></div>

    <svg class="frame" viewBox="0 0 1200 804" aria-hidden="true">
      <g fill="none" stroke="var(--frame)" stroke-width="1.5">
        <polyline points="69,129 69,67 1131,67 1131,129"/>
        <polyline points="66,676 66,739 129,739"/>
        <polyline points="1134,676 1134,739 1071,739"/>
      </g>
    </svg>

    <header class="brand">
      <h1 class="brand-name">Crowns in the Sky</h1>
      <p class="brand-owner">by Lena Marchetti</p>
    </header>

    <div class="divider"></div>

    <p class="contact contact-address">5/27 Harlow Street, Maleny</p>
    <p class="contact contact-web">www.crownsinthesky.com</p>
  </main>
</body>
</html>
```